Keystone STEM Academy by graduating students from college in two years

Based on the logo design, create stationary and business cards for
Dr. Velimir T Osunde, CEO, (571) 482-1630
and Mirela Thorpe, Respresentative, (240) 557-2048
Address: 4417 Marbleton Lane, Alderwick Station, MD 22061
Incorporate elelments of the logo

Target Market(s)

USA

Other font styles liked:
• match with the logo type style

```html
<!DOCTYPE html>
<html lang="en">
<head>
<meta charset="utf-8">
<title>Keystone STEM Academy – Letterhead</title>
<link rel="stylesheet" href="https://fonts.googleapis.com/css2?family=Tinos:wght@400;700&display=swap">
<style>
  :root {
    --navy: #0c2260;
    --gold: #f6c531;
    --ink: #111111;
    --paper: #ffffff;
    --backdrop: #9a9b9c;
  }
  * { margin: 0; padding: 0; box-sizing: border-box; }
  html, body {
    width: 1200px; height: 816px; overflow: hidden;
    background: var(--backdrop);
    font-family: "Tinos", "Times New Roman", serif;
  }
  .letterhead {
    position: absolute; left: 300px; top: 20px;
    width: 600px; height: 776px;
    background: var(--paper);
    box-shadow: 0 6px 24px rgba(0,0,0,.25);
    overflow: hidden;
  }
  .side-bar {
    position: absolute; left: 0; width: 48px; height: 26px;
    background: var(--navy);
  }
  .side-bar--upper { top: 72px; }
  .side-bar--lower { top: 112px; }

  .brand {
    position: absolute; left: 56px; top: 74px; width: 96px;
    display: flex; flex-direction: column; align-items: center; gap: 6px;
    text-align: center;
  }
  .brand__dot { width: 14px; height: 14px; border-radius: 50%; background: var(--gold); }
  .brand__name {
    color: var(--navy); font-weight: 700; font-size: 13px; line-height: 1.15;
  }

  .contact {
    position: absolute; left: 160px; height: 28px;
    display: flex; align-items: center;
  }
  .contact--ceo { top: 70px; }
  .contact--rep { top: 108px; }
  .contact__tab { width: 26px; height: 22px; background: var(--navy); }
  .contact__rule { width: 4px; height: 26px; background: var(--gold); margin: 0 8px 0 6px; }
  .contact__name { color: var(--navy); font-weight: 700; font-size: 12.5px; line-height: 1.1; }
  .contact__role { color: var(--navy); font-size: 11.5px; line-height: 1.15; }

  .header-rule {
    position: absolute; left: 160px; right: 0; height: 1px;
  }
  .header-rule--navy { top: 148px; background: var(--navy); }
  .header-rule--gold { top: 152px; background: var(--gold); }

  .corner-bar {
    position: absolute; top: 0; width: 22px; height: 50px; background: var(--navy);
  }
  .corner-bar--left { left: 505px; }
  .corner-bar--right { left: 540px; }
  .corner-tick {
    position: absolute; top: 56px; width: 22px; height: 3px; background: var(--gold);
  }
  .corner-tick--left { left: 505px; }
  .corner-tick--right { left: 540px; }

  .footer-band {
    position: absolute; left: 0; right: 0; top: 698px; height: 30px;
    background: var(--gold);
    display: flex; align-items: center; justify-content: center;
  }
  .footer-band__address { color: var(--ink); font-size: 13px; }
</style>
</head>
<body>
  <main class="letterhead">
    <div class="side-bar side-bar--upper"></div>
    <div class="side-bar side-bar--lower"></div>

    <div class="brand">
      <span class="brand__dot"></span>
      <span class="brand__name">Keystone STEM Academy</span>
    </div>

    <div class="contact contact--ceo">
      <span class="contact__tab"></span>
      <span class="contact__rule"></span>
      <div>
        <p class="contact__name">Dr. Velimir T Osunde</p>
        <p class="contact__role">CEO, (571) 482-1630</p>
      </div>
    </div>
    <div class="contact contact--rep">
      <span class="contact__tab"></span>
      <span class="contact__rule"></span>
      <div>
        <p class="contact__name">Mirela Thorpe</p>
        <p class="contact__role">Respresentative, (240) 557-2048</p>
      </div>
    </div>

    <div class="header-rule header-rule--navy"></div>
    <div class="header-rule header-rule--gold"></div>

    <div class="corner-bar corner-bar--left"></div>
    <div class="corner-bar corner-bar--right"></div>
    <div class="corner-tick corner-tick--left"></div>
    <div class="corner-tick corner-tick--right"></div>

    <footer class="footer-band">
      <p class="footer-band__address">4417 Marbleton Lane, Alderwick Station, MD 22061</p>
    </footer>
  </main>
</body>
</html>
```